Webdesign Tischlerei Wallbusch
Zielgruppe
es handelt sich um eine Tischlerei / Meisterbetrieb
Zielgruppe: private und gwerbliche Kunden
Aufgabenstellung
- die Vielfältigkeit der Produkte aus eigener Herstellung durch Meisterhand soll vermittelt werden
- FixWerk Systemspezialist
- Produktschulungen Kork
- KEINE Kopie der alten Seite
- aufgelockert und modern
- gern mit Elementen in leichter Holzoptik und weichen Rundungen
- Farben modern und in Telen an das Logo angepasst
Vorstellung des Kunden zur Navigationsstruktur:
Navigationsstruktur Website
1. wo arbeiten wir... (in der Werkstatt findet mittlerweile der geringere Anteil der Arbeit statt)
• Bild Werkstatt von außen/Schild
• Mitarbeiter an der Säge
• und/oder Mitarbeiter an der Hobelmaschine
• Gespräch/Planung/Skizzen
• evtl. (gepacktes) Fahrzeug(denn das ist ein wichtiges Arbeitsmittel)
2. was macht uns aus...
• vernünftiges Verhältnis zu den Mitarbeitern, ermöglicht eine kontinuierliche, fachgerechte und qualitativ hochwertige Arbeit an den Projekten
• überwiegend handwerkliche Fertigung
• Verwendung von Materialien und Hölzern- auch aus der Region
• Flexibilität im Umgang mit Arbeitszeit, Material und Leistungen
3. welche Möglichkeiten haben wir....
• „Liste“ mit den Möglichkeiten die wir so haben(z.B. Herstellung und Reparaturen von individuellen Treppen, Möbeln, Türen, Lieferung und Reparatur von Fenstern, verlegen und reparieren von Fußböden wie Hobeldielen, Parkett, Designböden, Carport, Zäune, Tore
• Galerie Projekte mit Beschreibung
• vorher-nachher Bilder mit Beschreibung
4. was sollte Sie interessieren...
• Tipps &Tricks rund ums Holz/Produkte(Fenster Pflegehinweise)
• Termine und Veranstaltungen auch nicht betrieblich
• Empfehlungen (Produkte, Materialien, Pflegemittel -was wir benutzen und gefällt oder ist das dann Werbung?)
5. womit könnten wir ihnen helfen...
• Interaktives Anfrageformular
• Möglichkeit Skizzen hochzuladen, Wünsche zu beschreiben
6. wie erreichen Sie uns...<..

```html
<!DOCTYPE html>
<html lang="de">
<head>
<meta charset="utf-8">
<title>Tischlerei Wallbusch</title>
<link href="https://fonts.googleapis.com/css2?family=Open+Sans:wght@400;600;700&family=Open+Sans+Condensed:wght@700&display=swap" rel="stylesheet">
<style>
:root{
  --bar:#3a332c;
  --header:#f7f6f3;
  --blue:#1565a8;
  --light:#ecebe8;
  --panel:#4a4139;
  --ink:#4a4642;
  --white:#ffffff;
  --wood-band:linear-gradient(90deg,#a97b4f 0%,#d2a877 12%,#b88858 24%,#e0bb8e 38%,#c09062 52%,#dcb283 66%,#b08256 80%,#d6ad7e 92%,#a97b4f 100%);
  --wood-card:linear-gradient(100deg,#e4c199 0%,#d3a677 18%,#ebcba4 34%,#d8ab7b 52%,#eccfaa 70%,#cf9f6d 86%,#e6c49c 100%);
}
*{box-sizing:border-box;margin:0;padding:0}
html,body{width:1200px;height:4262px;overflow:hidden}
body{font-family:"Open Sans",Arial,sans-serif;background:var(--light);position:relative;color:var(--ink)}
.abs{position:absolute}
.nowrap{white-space:nowrap}
.topbar{left:0;top:0;width:1200px;height:12px;background:var(--bar)}
.header{left:0;top:12px;width:1200px;height:63px;background:var(--header)}
.brand{left:265px;top:31px;font-weight:700;font-size:19px;color:var(--blue);letter-spacing:.5px}
.head-phone{left:712px;top:38px;font-size:14px;font-weight:600;color:#333;display:flex;align-items:center;gap:6px}
.head-dot{left:854px;top:36px;width:20px;height:20px;border:2px solid #333;border-radius:50%}
.burger{left:910px;top:39px;width:22px}
.burger span{display:block;height:3px;background:var(--blue);margin-bottom:4px;border-radius:2px}

.page{left:0;top:75px;width:809px;height:4187px;overflow:hidden;filter:blur(1.2px)}
.dim{left:0;top:75px;width:809px;height:4187px;background:rgba(62,52,42,.55)}
.photo{border-radius:8px;box-shadow:0 2px 6px rgba(0,0,0,.25)}
.hero-img{left:0;top:0;width:809px;height:367px;background:radial-gradient(ellipse at 78% 40%,#d8c0a2 0%,#a88462 30%,transparent 60%),linear-gradient(90deg,#3a2e24 0%,#5a4634 45%,#8e6e50 75%,#c2a282 100%)}
.hero-band{left:0;top:367px;width:809px;height:126px;background:#e2e0dc}
.hero-title{left:265px;top:88px;font-family:"Open Sans Condensed","Open Sans",sans-serif;font-size:30px;color:#fff;font-weight:700}
.hero-text{left:265px;top:135px;width:240px;font-size:13px;line-height:17px;color:#eee}
.ghost-btn{left:268px;top:252px;width:154px;height:28px;border:2px solid #ddd;border-radius:14px;color:#eee;font-size:12px;text-align:center;line-height:24px}
.feature{width:148px;height:118px;border-radius:12px;background:#f3f2ef;text-align:center;font-size:11px;font-weight:600;color:#777;padding:62px 10px 0;line-height:15px;box-shadow:0 2px 5px rgba(0,0,0,.15)}
.feature.active{background:var(--blue);color:#fff}
.feature svg{position:absolute;left:52px;top:12px}

.sec-title{font-family:"Open Sans Condensed","Open Sans",sans-serif;font-weight:700;font-size:34px;color:var(--ink)}
.sec-intro{font-size:13px;line-height:17px;color:#666;text-align:center;width:480px}
.card-img{width:210px;height:170px}
.card-title{font-family:"Open Sans Condensed","Open Sans",sans-serif;font-weight:700;font-size:20px;line-height:20px;color:var(--ink);width:210px}
.card-text{font-size:13px;line-height:17px;color:#666;width:210px}
.more{font-size:13px;font-weight:700;color:var(--ink)}
.wood-band{left:0;width:809px;background:var(--wood-band)}
.gallery{left:0;top:1208px;width:809px;height:1092px;background:linear-gradient(90deg,#4a3828 0%,#5e4630 20%,#4e3a2a 40%,#654b34 60%,#4c392a 80%,#5a4430 100%)}
.gal-img{border-radius:2px;box-shadow:0 3px 8px rgba(0,0,0,.35)}
.btn{background:var(--blue);color:#fff;font-weight:700;font-size:13px;text-align:center;border-radius:16px}
.work{left:0;top:2300px;width:809px;height:563px;background:var(--light)}
.interest-bg{left:0;top:2917px;width:809px;height:682px;background:var(--wood-band)}
.interest-panel{left:53px;top:2970px;width:800px;height:579px;background:#ecebe8;border-radius:4px}
.footer{left:0;top:3657px;width:809px;height:530px;background:#2f2a25}
.foot-brand{left:380px;top:3745px;font-size:40px;font-weight:700;color:#fff;letter-spacing:1px}
.foot-box{top:3839px;height:212px;border-radius:4px;background:var(--wood-card);padding:18px 22px;color:#fff;font-size:15px;line-height:22px;overflow:hidden}

.panel{left:809px;top:75px;width:391px;height:4187px;background:var(--panel)}
.panel-title{left:837px;top:110px;font-size:33px;line-height:40px;color:#fff;font-weight:400}
.panel-nav{left:840px;top:242px;list-style:none}
.panel-nav li{font-size:21px;color:#fff;height:45.5px;display:flex;gap:10px;white-space:nowrap}
.panel-btn{left:844px;top:508px;width:288px;height:43px;line-height:43px;font-size:17px;border-radius:22px;box-shadow:0 3px 5px rgba(0,0,0,.35)}
.contact-card{left:839px;top:642px;width:334px;height:296px;background:var(--wood-card);padding:22px 22px;color:#fff;box-shadow:0 2px 6px rgba(0,0,0,.3)}
.contact-card h2{font-family:"Open Sans Condensed","Open Sans",sans-serif;font-size:28px;line-height:28px;font-weight:700;width:230px}
.contact-card p{font-size:20px;line-height:28px;margin-top:26px}
.contact-card .tel{font-size:20px;line-height:27px;margin-top:26px}
.legal{left:841px;top:972px;font-size:12px;color:#c9c3bb;letter-spacing:.3px}
</style>
</head>
<body>
<div class="abs topbar"></div>
<header class="abs header"></header>
<div class="abs brand nowrap">TISCHLEREI WALLBUSCH</div>
<div class="abs head-phone">
  <svg width="16" height="16" viewBox="0 0 24 24"><path fill="#222" d="M6.6 10.8a15 15 0 0 0 6.6 6.6l2.2-2.2c.3-.3.7-.4 1-.2 1.1.4 2.3.6 3.6.6.6 0 1 .4 1 1V20c0 .6-.4 1-1 1A17 17 0 0 1 3 4c0-.6.4-1 1-1h3.5c.6 0 1 .4 1 1 0 1.3.2 2.5.6 3.6.1.3 0 .7-.2 1z"/></svg>
  012345 67890
</div>
<div class="abs head-dot"></div>
<div class="abs burger"><span></span><span></span><span></span></div>

<main class="abs page">
  <section>
    <div class="abs hero-img" role="img" aria-label="Hände bei der Arbeit mit einem Handhobel an Holz"></div>
    <div class="abs hero-band"></div>
    <h1 class="abs hero-title">WAS MACHT UNS AUS?</h1>
    <p class="abs hero-text">Lorem ipsum dolor sit amet, consectetur adipiscing elit, sed do eiusmod tempor incididunt ut labore et dolore magna aliqua. Quis ipsum suspendisse ultrices gravida.</p>
    <div class="abs ghost-btn">» mehr über uns</div>
    <svg class="abs" style="left:45px;top:140px" width="40" height="70"><path d="M34 4 6 35l28 31" fill="none" stroke="#aaa" stroke-width="7"/></svg>
    <div class="abs feature active" style="left:365px;top:322px">
      <svg width="44" height="44" viewBox="0 0 44 44" fill="none" stroke="currentColor" stroke-width="3" stroke-linecap="round"><path d="M8 36 30 14"/><path d="M28 8a7 7 0 0 0 8 8l-4 4-8-8z"/><path d="M36 36 14 14"/><path d="M10 8l6 6-2 2-6-6z"/></svg>
      Überwiegend handwerkliche Fertigung</div>
    <div class="abs feature" style="left:526px;top:339px">
      <svg width="44" height="44" viewBox="0 0 44 44" fill="none" stroke="currentColor" stroke-width="3" stroke-linecap="round"><circle cx="16" cy="26" r="10"/><circle cx="16" cy="26" r="4"/><circle cx="30" cy="16" r="9"/><circle cx="30" cy="16" r="3"/></svg>
      Materialien &amp; Hölzer aus der Region</div>
    <div class="abs feature" style="left:686px;top:339px">
      <svg width="44" height="44" viewBox="0 0 44 44" fill="none" stroke="currentColor" stroke-width="3" stroke-linecap="round"><path d="M10 18a13 13 0 0 1 23-6"/><path d="M34 6v7h-7"/><path d="M34 26a13 13 0 0 1-23 6"/><path d="M10 38v-7h7"/></svg>
      Kunden-orientierte Flexibilität</div>
  </section>

  <section>
    <h2 class="abs sec-title" style="left:463px;top:532px">Unsere Möglichkeiten</h2>
    <p class="abs sec-intro" style="left:360px;top:590px">Lorem ipsum dolor sit amet, consectetur adipiscing elit, sed do eiusmod tempor incididunt ut labore et dolore magna aliqua. Quis ipsum suspendisse gravida. Risus commodo viverra maecenas accumsan lacus vel facilisis.</p>
    <div class="abs card-img photo" style="left:268px;top:686px;background:radial-gradient(circle at 45% 45%,#c9a67e 0%,transparent 45%),linear-gradient(135deg,#3e2f22,#7a5c40 60%,#b39068)" role="img" aria-label="Handwerker beim Hobeln"></div>
    <div class="abs card-img photo" style="left:493px;top:686px;background:radial-gradient(circle at 70% 60%,#d49a64 0%,transparent 50%),linear-gradient(160deg,#6a3e20,#a8642e 55%,#c98449)" role="img" aria-label="Holzoberfläche wird poliert"></div>
    <div class="abs card-img photo" style="left:720px;top:686px;background:linear-gradient(135deg,#9a7a58,#dcc2a0 50%,#a8865e)" role="img" aria-label="Montage einer Holzkonstruktion"></div>
    <h3 class="abs card-title" style="left:268px;top:880px">Handwerkliche Herstellung</h3>
    <h3 class="abs card-title" style="left:493px;top:880px">Reparatur und Instandsetzung</h3>
    <h3 class="abs card-title" style="left:720px;top:880px">Montage</h3>
    <p class="abs card-text" style="left:268px;top:932px">Lorem ipsum dolor sit amet, consectetur adipiscing elit, sed do eiusmod tempor incididunt ut labore et dolore magna aliqua. Quis ipsum suspendisse ultrices gravida.</p>
    <p class="abs card-text" style="left:493px;top:932px">Lorem ipsum dolor sit amet, consectetur adipiscing elit, sed do eiusmod tempor incididunt ut labore et dolore magna aliqua. Quis ipsum suspendisse ultrices gravida.</p>
    <p class="abs card-text" style="left:720px;top:915px">Lorem ipsum dolor sit amet, consectetur adipiscing elit, sed do eiusmod tempor incididunt ut labore et dolore magna aliqua. Quis ipsum suspendisse gravida.</p>
    <span class="abs more" style="left:268px;top:1054px">» mehr Infos</span>
    <span class="abs more" style="left:493px;top:1054px">» mehr Infos</span>
    <span class="abs more" style="left:720px;top:1038px">» mehr Infos</span>
  </section>

  <div class="abs wood-band" style="top:1150px;height:58px"></div>

  <section class="abs gallery">
    <h2 class="abs sec-title" style="left:475px;top:70px;color:#eee">Unsere Galerie</h2>
    <p class="abs sec-intro" style="left:360px;top:125px;color:#ccc">Lorem ipsum dolor sit amet, consectetur adipiscing elit, sed do eiusmod tempor incididunt ut labore et dolore magna aliqua. Quis ipsum suspendisse gravida. Risus commodo viverra maecenas accumsan lacus vel facilisis.</p>
    <div class="abs gal-img" style="left:99px;top:218px;width:320px;height:319px;background:linear-gradient(160deg,#a0907a 0%,#d8c8ae 40%,#c2ab88 70%,#a88a64)" role="img" aria-label="Einbauschrank unter Dachschräge"></div>
    <div class="abs gal-img" style="left:439px;top:218px;width:321px;height:295px;background:linear-gradient(150deg,#c8beb0 0%,#eee8de 45%,#d4bc98 80%,#b89a72)" role="img" aria-label="Holztreppe im Dachgeschoss"></div>
    <div class="abs gal-img" style="left:778px;top:218px;width:31px;height:238px;background:linear-gradient(180deg,#c09060,#8a6a48)" role="img" aria-label="Weiteres Projektbild"></div>
    <div class="abs gal-img" style="left:99px;top:561px;width:320px;height:336px;background:linear-gradient(170deg,#8c7c64 0%,#b89a74 40%,#c89c68 60%,#7e8a84 100%)" role="img" aria-label="Küche mit Holzarbeitsplatte"></div>
    <div class="abs gal-img" style="left:439px;top:541px;width:321px;height:432px;background:radial-gradient(ellipse at 50% 30%,#c08a54 0%,transparent 55%),linear-gradient(180deg,#7a4c28,#a06a3a 50%,#6e4424)" role="img" aria-label="Massivholzschrank"></div>
    <div class="abs gal-img" style="left:778px;top:480px;width:31px;height:262px;background:linear-gradient(180deg,#6a7a50,#8a6a4e)" role="img" aria-label="Weiteres Projektbild"></div>
    <div class="abs btn" style="left:508px;top:1022px;width:184px;height:30px;line-height:30px">» weitere Projekte</div>
  </section>

  <section class="abs work">
    <h2 class="abs sec-title" style="left:268px;top:222px">Wo arbeiten wir?</h2>
    <p class="abs card-text" style="left:268px;top:278px;width:215px">Lorem ipsum dolor sit amet, consectetur adipiscing elit, sed do eiusmod tempor incididunt ut labore et dolore magna aliqua. Quis ipsum suspendisse ultrices gravida. Risus commodo viverra maecenas accumsan lacus vel facilisis.</p>
    <div class="abs btn" style="left:268px;top:472px;width:154px;height:30px;line-height:30px">» mehr Infos</div>
    <div class="abs" style="left:551px;top:136px;width:210px;height:349px;background:linear-gradient(180deg,#8a7a64 0%,#5a5048 40%,#2e2c2c 70%,#a07850 100%)" role="img" aria-label="Tischlermeister in der Werkstatt"></div>
    <div class="abs" style="left:766px;top:136px;width:43px;height:349px;background:linear-gradient(180deg,#9a8870,#6a5a48)" role="img" aria-label="Werkstattansicht"></div>
  </section>

  <div class="abs interest-bg"></div>
  <section class="abs interest-panel">
    <h2 class="abs nowrap" style="left:370px;top:55px;font-weight:400;font-family:'Open Sans Condensed','Open Sans',sans-serif;font-size:30px;color:var(--ink)">Was sollte Sie interessieren?</h2>
    <div class="abs card-img photo" style="left:215px;top:118px;background:linear-gradient(170deg,#b88a58,#e2c49c 45%,#a4764a)" role="img" aria-label="Gestapelte Holzbretter"></div>
    <div class="abs card-img photo" style="left:440px;top:118px;background:radial-gradient(circle at 55% 45%,#e8d4b8 0%,#b08058 30%,#6a4428 70%)" role="img" aria-label="Tasse Kaffee"></div>
    <div class="abs card-img photo" style="left:667px;top:118px;background:linear-gradient(135deg,#8a5a30,#c48e58 50%,#7a4c26)" role="img" aria-label="Holzwerkzeuge"></div>
    <h3 class="abs card-title" style="left:215px;top:323px">Tipps &amp; Tricks</h3>
    <h3 class="abs card-title" style="left:440px;top:323px">Termine &amp; Veranstaltungen</h3>
    <h3 class="abs card-title" style="left:667px;top:323px">Empfehlungen</h3>
    <p class="abs card-text" style="left:215px;top:355px">Lorem ipsum dolor sit amet, consectetur adipiscing elit, sed do eiusmod tempor incididunt ut labore et dolore magna aliqua. Quis ipsum suspendisse ultrices gravida.</p>
    <p class="abs card-text" style="left:440px;top:372px">Lorem ipsum dolor sit amet, consectetur adipiscing elit, sed do eiusmod tempor incididunt ut labore et dolore magna aliqua. Quis ipsum suspendisse ultrices gravida.</p>
    <p class="abs card-text" style="left:667px;top:355px">Lorem ipsum dolor sit amet, consectetur adipiscing elit, sed do eiusmod tempor.</p>
    <span class="abs more" style="left:215px;top:480px">» mehr Infos</span>
    <span class="abs more" style="left:440px;top:497px">» mehr Infos</span>
    <span class="abs more" style="left:667px;top:480px">» mehr Infos</span>
  </section>

  <footer class="abs footer"></footer>
  <div class="abs foot-brand nowrap">TISCHLEREI WALLBUSCH</div>
  <div class="abs foot-box" style="left:270px;width:263px">Meisterbetrieb<br>Tischlerei Wallbusch<br><br>Holzgasse 7<br>01234 Musterdorf<br>012345 67890<br>012345 67891</div>
  <div class="abs foot-box" style="left:558px;width:260px"><span style="font-size:26px;line-height:28px;display:block">Womit können Ihnen helfen?</span><span style="font-size:12px;line-height:15px;display:block;margin-top:8px">Lorem ipsum dolor sit amet, consectetur adipiscing elit, sed do eiusmod tempor.</span></div>
  <div class="abs btn" style="left:593px;top:3995px;width:216px;height:30px;line-height:30px">» zum Anfrage-Formular</div>
  <div class="abs wood-band" style="top:4128px;height:59px"></div>
</main>
<div class="abs dim"></div>

<aside class="abs panel"></aside>
<h2 class="abs panel-title">Wie können wir<br>helfen?</h2>
<ul class="abs panel-nav">
  <li><span>&gt;</span>Was macht uns aus?</li>
  <li><span>&gt;</span>Unsere Möglichkeiten</li>
  <li><span>&gt;</span>Wo arbeiten wir?</li>
  <li><span>&gt;</span>Was sollte Sie interessieren?</li>
  <li><span>&gt;</span>Womit können wir Ihnen helfen?</li>
</ul>
<div class="abs btn panel-btn">» zum Anfrage-Formular</div>
<div class="abs contact-card">
  <h2>Meisterbetrieb Tischlerei Wallbusch</h2>
  <p>Holzgasse 7<br>01234 Musterdorf</p>
  <div class="tel">
    <div><svg width="14" height="14" viewBox="0 0 24 24"><path fill="#3a2e24" d="M6.6 10.8a15 15 0 0 0 6.6 6.6l2.2-2.2c.3-.3.7-.4 1-.2 1.1.4 2.3.6 3.6.6.6 0 1 .4 1 1V20c0 .6-.4 1-1 1A17 17 0 0 1 3 4c0-.6.4-1 1-1h3.5c.6 0 1 .4 1 1 0 1.3.2 2.5.6 3.6.1.3 0 .7-.2 1z"/></svg> 012345 67890</div>
    <div><svg width="14" height="14" viewBox="0 0 24 24"><path fill="#3a2e24" d="M6 3h12v5H6zM3 9h18v8h-3v4H6v-4H3zm5 6v4h8v-4z"/></svg> 012345 67891</div>
  </div>
</div>
<div class="abs legal">IMPRESSUM | DATENSCHUTZ</div>
</body>
</html>
```